Business Card Design

Hunting Ranch in the Texas hill country (Deer, Turkey, Quail)

Want Walter on one side and Gloria on the other.
We are looking for a Jack Rabbit NOT a cottontail bunny

Industry/Entity Type

Business

Contact Information for Business Card

Copper Mesa Ranch
Junction Texas
Walter Krimsley Gloria Krimsley
14 Paloverde Hollow Ct. 14 Paloverde Hollow Ct.
Cedar Bluff, Texas U.S.A. Cedar Bluff, Texas U.S.A.
281-555-0143 281-555-0187

```html
<!DOCTYPE html>
<html lang="en">
<head>
<meta charset="utf-8">
<title>Copper Mesa Ranch – Business Cards</title>
<link rel="stylesheet" href="https://fonts.googleapis.com/css2?family=Didact+Gothic&family=Open+Sans:wght@400&display=swap">
<style>
  :root {
    --backdrop: #474847;
    --card-light: #f7f7f5;
    --card-dark: #262626;
    --ink-dark: #2b2b2b;
    --ink-light: #d9d9d9;
    --copper: #8b4a26;
    --copper-bright: #b0683a;
    --wordmark-light: #5a5a5a;
    --wordmark-dark: #cfcfcf;
  }
  * { box-sizing: border-box; margin: 0; padding: 0; }
  html, body {
    width: 1200px; height: 1066px; overflow: hidden;
    background: var(--backdrop);
  }
  .sheet {
    width: 1200px; height: 1066px;
    display: flex; flex-direction: column; align-items: center; justify-content: center;
    gap: 56px;
  }
  .card {
    position: relative;
    width: 760px; height: 434px;
    overflow: hidden;
    box-shadow: 0 10px 30px rgba(0,0,0,0.35);
  }
  .card--light { background: var(--card-light); color: var(--ink-dark); }
  .card--dark { background: var(--card-dark); color: var(--ink-light); }

  .brand {
    position: absolute; right: 70px; top: 130px;
    display: flex; align-items: center; gap: 14px;
    white-space: nowrap;
  }
  .brand__dot {
    width: 26px; height: 26px; border-radius: 50%;
    background: var(--copper);
    flex: none;
  }
  .card--dark .brand__dot { background: var(--copper-bright); }
  .brand__name {
    font-family: "Didact Gothic", sans-serif;
    font-size: 34px; line-height: 1;
    color: var(--wordmark-light);
  }
  .card--dark .brand__name { color: var(--wordmark-dark); }

  .contact {
    position: absolute; left: 120px; top: 258px;
    font-family: "Didact Gothic", sans-serif;
    white-space: nowrap;
  }
  .contact__name {
    font-family: "Open Sans", sans-serif;
    font-size: 27px; line-height: 1.3; margin-bottom: 10px;
  }
  .card--dark .contact__name { font-family: "Didact Gothic", sans-serif; }
  .contact__row {
    display: flex; align-items: flex-start; gap: 12px;
    font-size: 19px; line-height: 1.35;
    margin-bottom: 10px;
  }
  .contact__icon { width: 16px; height: 22px; flex: none; margin-top: 2px; }
  .contact__icon path, .contact__icon rect, .contact__icon circle {
    fill: none; stroke: var(--copper); stroke-width: 1.8;
  }
  .card--dark .contact__icon path,
  .card--dark .contact__icon rect,
  .card--dark .contact__icon circle { stroke: var(--copper-bright); }
</style>
</head>
<body>
<main class="sheet">

  <section class="card card--light" aria-label="Business card for Walter Krimsley">
    <div class="brand">
      <span class="brand__dot"></span>
      <span class="brand__name">Copper Mesa Ranch</span>
    </div>
    <div class="contact">
      <p class="contact__name">Walter Krimsley</p>
      <div class="contact__row">
        <svg class="contact__icon" viewBox="0 0 16 22" aria-hidden="true">
          <path d="M8 21 C3 14 1.5 11 1.5 7.5 A6.5 6.5 0 0 1 14.5 7.5 C14.5 11 13 14 8 21 Z"/>
          <circle cx="8" cy="7.5" r="2.3"/>
        </svg>
        <p>14 Paloverde Hollow Ct. 14 Paloverde Hollow Ct.<br>Cedar Bluff, Texas U.S.A.</p>
      </div>
      <div class="contact__row">
        <svg class="contact__icon" viewBox="0 0 16 22" aria-hidden="true">
          <rect x="2" y="1.5" width="12" height="19" rx="2"/>
          <path d="M6 17.5 H10"/>
        </svg>
        <p>281-555-0143</p>
      </div>
    </div>
  </section>

  <section class="card card--dark" aria-label="Business card for Gloria Krimsley">
    <div class="brand">
      <span class="brand__dot"></span>
      <span class="brand__name">Copper Mesa Ranch</span>
    </div>
    <div class="contact">
      <p class="contact__name">Gloria Krimsley</p>
      <div class="contact__row">
        <svg class="contact__icon" viewBox="0 0 16 22" aria-hidden="true">
          <path d="M8 21 C3 14 1.5 11 1.5 7.5 A6.5 6.5 0 0 1 14.5 7.5 C14.5 11 13 14 8 21 Z"/>
          <circle cx="8" cy="7.5" r="2.3"/>
        </svg>
        <p>14 Paloverde Hollow Ct. 14 Paloverde Hollow Ct.<br>Cedar Bluff, Texas U.S.A.</p>
      </div>
      <div class="contact__row">
        <svg class="contact__icon" viewBox="0 0 16 22" aria-hidden="true">
          <rect x="2" y="1.5" width="12" height="19" rx="2"/>
          <path d="M6 17.5 H10"/>
        </svg>
        <p>281-555-0187</p>
      </div>
    </div>
  </section>

</main>
</body>
</html>
```